PELDRAX Business Cards

We require a business card for our company that provides IT consulting services. We already have a logo that needs to be used on the card. We want a clean professional looking design that incorporates our colours. Our main focus is providing managed services to business, which involves us looking after all of their IT requirements including managing servers/networks, projects, and procurement.

Industry/Entity Type

Information Technology

Requirements
Must have
• our logo, contact information, name, title, phone numbers

```html
<!DOCTYPE html>
<html lang="en">
<head>
<meta charset="utf-8">
<title>PELDRAX Business Cards</title>
<link rel="stylesheet" href="https://fonts.googleapis.com/css2?family=Montserrat:wght@300;400;600;700&family=Quicksand:wght@400;500&display=swap">
<style>
  :root {
    --brand-blue: #1b90cc;
    --paper: #ffffff;
    --canvas-bg: #ffffff;
    --card-edge: #d9d9d9;
    --ink-light: #ffffff;
    --ink-soft: #d6ecf8;
  }
  html, body {
    margin: 0;
    padding: 0;
    width: 1200px;
    height: 1000px;
    overflow: hidden;
    background: var(--canvas-bg);
  }
  .canvas {
    position: relative;
    width: 1200px;
    height: 1000px;
    font-family: "Montserrat", Arial, sans-serif;
  }
  .card {
    position: absolute;
    top: 348px;
    width: 472px;
    height: 305px;
    box-sizing: border-box;
  }
  .card-front {
    left: 101px;
    background: var(--paper);
    border: 1px solid var(--card-edge);
  }
  .card-back {
    left: 627px;
    background: var(--brand-blue);
  }

  /* front: brand name */
  .brand {
    position: absolute;
    right: 26px;
    top: 62px;
    display: flex;
    align-items: center;
    gap: 10px;
    color: var(--brand-blue);
    font-weight: 600;
    font-size: 30px;
    letter-spacing: 0.5px;
    line-height: 1;
  }
  .brand-dot {
    width: 22px;
    height: 22px;
    border-radius: 50%;
    background: var(--brand-blue);
  }

  /* front: blue info band */
  .info-band {
    position: absolute;
    left: 27px;
    top: 120px;
    width: 417px;
    height: 154px;
    background: var(--brand-blue);
    color: var(--ink-light);
  }
  .person {
    position: absolute;
    left: 15px;
    top: 19px;
  }
  .person-name {
    margin: 0;
    font-size: 14.5px;
    font-weight: 600;
    line-height: 18px;
  }
  .person-title {
    margin: 0;
    font-size: 12.5px;
    font-weight: 300;
    color: var(--ink-soft);
    line-height: 16px;
  }
  .contact-list {
    position: absolute;
    left: 233px;
    top: 21px;
    margin: 0;
    padding: 0;
    list-style: none;
  }
  .contact-item {
    display: flex;
    align-items: center;
    height: 18.5px;
    font-size: 11.5px;
    font-weight: 300;
  }
  .contact-icon {
    width: 11px;
    height: 11px;
    margin-right: 8px;
    flex: none;
  }
  .social-mark-circle {
    width: 8px;
    height: 8px;
    margin: 0 10px 0 1px;
    border-radius: 50%;
    background: var(--ink-light);
    flex: none;
  }
  .social-mark-square {
    width: 9px;
    height: 9px;
    margin: 0 9px 0 1px;
    border: 1.2px solid var(--ink-light);
    border-radius: 2px;
    box-sizing: border-box;
    flex: none;
  }

  /* back: website line */
  .web-line {
    position: absolute;
    left: 0;
    right: 0;
    top: 142px;
    text-align: center;
    color: var(--ink-light);
    font-family: "Quicksand", "Montserrat", sans-serif;
    font-weight: 500;
    font-size: 17px;
    letter-spacing: 5px;
    margin: 0;
  }
</style>
</head>
<body>
<main class="canvas">

  <section class="card card-front" aria-label="Business card front">
    <div class="brand">
      <span class="brand-dot"></span>
      <span class="brand-name">PELDRAX</span>
    </div>

    <div class="info-band">
      <div class="person">
        <p class="person-name">Name SURNAME</p>
        <p class="person-title">Title</p>
      </div>

      <ul class="contact-list">
        <li class="contact-item">
          <svg class="contact-icon" viewBox="0 0 12 12" aria-hidden="true"><path d="M6 0.5a3.8 3.8 0 0 0-3.8 3.8C2.2 7.2 6 11.5 6 11.5s3.8-4.3 3.8-7.2A3.8 3.8 0 0 0 6 0.5zm0 5.2a1.5 1.5 0 1 1 0-3 1.5 1.5 0 0 1 0 3z" fill="#fff"/></svg>
          Adress
        </li>
        <li class="contact-item">
          <svg class="contact-icon" viewBox="0 0 12 12" aria-hidden="true"><rect x="1" y="2.5" width="10" height="7" rx="0.8" fill="#fff"/><path d="M1.3 3l4.7 3.4L10.7 3" fill="none" stroke="#1b90cc" stroke-width="0.9"/></svg>
          name@peldrax.com
        </li>
        <li class="contact-item">
          <svg class="contact-icon" viewBox="0 0 12 12" aria-hidden="true"><path d="M3 1l1.8 2.3-1 1.2c.6 1.4 1.6 2.5 3 3.1l1.2-1L10.5 8.5 9.6 10.4C5.3 10.2 1.7 6.6 1.5 2.2z" fill="none" stroke="#fff" stroke-width="1"/></svg>
          (123) 456-7891
        </li>
        <li class="contact-item">
          <span class="social-mark-circle"></span>
          peldrax
        </li>
        <li class="contact-item">
          <span class="social-mark-square"></span>
          peldrax
        </li>
        <li class="contact-item">
          <svg class="contact-icon" viewBox="0 0 12 12" aria-hidden="true"><g fill="none" stroke="#fff" stroke-width="0.9"><circle cx="6" cy="6" r="4.8"/><ellipse cx="6" cy="6" rx="2" ry="4.8"/><path d="M1.2 6h9.6M2 3.5h8M2 8.5h8"/></g></svg>
          www.peldrax.com
        </li>
      </ul>
    </div>
  </section>

  <section class="card card-back" aria-label="Business card back">
    <p class="web-line">www.peldrax.com</p>
  </section>

</main>
</body>
</html>
```